Corkbell Cellars: the premier wine registry - (need business cards)

We have a logo designed, and now we need business cards for our 3 founders. Corkbell Cellars is the premier wine registry for weddings. I am envisioning the wine glass with the heart in it as our signature symbol. (FYI- on the red background file, only use the part that has the red background; the brown colors are not relevant)

```html
<!DOCTYPE html>
<html lang="en">
<head>
<meta charset="utf-8">
<title>Corkbell Cellars – Business Cards</title>
<link href="https://fonts.googleapis.com/css2?family=Josefin+Sans:wght@300;400;700&display=swap" rel="stylesheet">
<style>
  :root {
    --bg: #2b2c30;
    --wine: #9e2252;
    --wine-deep: #861a44;
    --paper: #ffffff;
    --ink: #2a2a2a;
    --soft: #f3eef0;
  }
  * { margin: 0; padding: 0; box-sizing: border-box; }
  html, body {
    width: 1200px; height: 900px; overflow: hidden;
    background: var(--bg);
    font-family: "Josefin Sans", sans-serif;
  }
  .stage {
    position: relative; width: 1200px; height: 900px;
  }
  .card {
    position: absolute; top: 307px;
    width: 500px; height: 286px;
    border-radius: 3px;
    overflow: hidden;
    box-shadow: 0 10px 30px rgba(0,0,0,.35);
  }
  /* Front */
  .card--front {
    left: 70px;
    background: var(--wine);
    display: flex; align-items: center; justify-content: center; gap: 14px;
  }
  .brand-dot {
    width: 14px; height: 14px; border-radius: 50%;
    background: var(--soft);
  }
  .brand-name {
    color: var(--soft);
    font-weight: 300;
    font-size: 30px;
    letter-spacing: 7px;
    text-transform: uppercase;
  }
  /* Back */
  .card--back {
    left: 630px;
    background: var(--paper);
  }
  .card--back svg.backdrop { position: absolute; inset: 0; }
  .person {
    position: absolute; top: 30px; left: 250px; width: 200px;
    text-align: center;
  }
  .person__name {
    color: var(--wine);
    font-weight: 700; font-size: 20px; letter-spacing: 1.5px;
    text-transform: uppercase;
  }
  .person__role {
    color: var(--ink);
    font-size: 12px; letter-spacing: 1.5px; margin-top: 4px;
    text-transform: uppercase;
  }
  .contact {
    position: absolute; top: 122px; left: 90px; width: 280px;
    text-align: center; list-style: none;
    color: var(--paper);
    font-size: 13px; letter-spacing: 1.2px; line-height: 22px;
    text-transform: uppercase;
  }
  .corner-mark {
    position: absolute; width: 12px; height: 12px; border-radius: 50%;
    background: var(--wine);
  }
  .corner-mark--top { top: 22px; left: 160px; }
  .corner-mark--side { top: 140px; right: 26px; }
</style>
</head>
<body>
<main class="stage">
  <section class="card card--front" aria-label="Card front">
    <span class="brand-dot"></span>
    <span class="brand-name">Corkbell Cellars</span>
  </section>

  <section class="card card--back" aria-label="Card back">
    <svg class="backdrop" width="500" height="286" viewBox="0 0 500 286">
      <path d="M0 108 C90 60 180 62 260 80 C360 104 440 180 470 286 L0 286 Z" fill="var(--wine)"/>
      <g class="contact-icons" stroke="var(--wine)" fill="none" stroke-width="1.6">
        <g transform="translate(190 76)">
          <circle r="14" fill="var(--paper)" stroke="var(--wine)" stroke-width="2"/>
          <circle r="10" fill="var(--wine)" stroke="none"/>
          <path d="M-5 -3 Q0 -7 5 -3 M-4 -1 L-4 4 L4 4 L4 -1" stroke="var(--paper)"/>
        </g>
        <g transform="translate(235 76)">
          <circle r="14" fill="var(--paper)" stroke="var(--wine)" stroke-width="2"/>
          <circle r="10" fill="var(--wine)" stroke="none"/>
          <rect x="-5.5" y="-3.5" width="11" height="7" stroke="var(--paper)"/>
          <path d="M-5.5 -3.5 L0 1 L5.5 -3.5" stroke="var(--paper)"/>
        </g>
        <g transform="translate(280 86)">
          <circle r="14" fill="var(--paper)" stroke="var(--wine)" stroke-width="2"/>
          <circle r="10" fill="var(--wine)" stroke="none"/>
          <circle r="5.5" stroke="var(--paper)"/>
          <ellipse rx="2.4" ry="5.5" stroke="var(--paper)"/>
          <path d="M-5.5 0 H5.5" stroke="var(--paper)"/>
        </g>
      </g>
    </svg>
    <span class="corner-mark corner-mark--top"></span>
    <span class="corner-mark corner-mark--side"></span>
    <div class="person">
      <p class="person__name">Marlow Keane</p>
      <p class="person__role">Partner</p>
    </div>
    <ul class="contact">
      <li>+01 555 014 2290</li>
      <li>hello@corkbellcellars.com</li>
      <li>www.corkbellcellars.com</li>
    </ul>
  </section>
</main>
</body>
</html>
```